"VaduMakers" Graphic Design Project

We are a new business creating bath/ body/beauty products. We need label designs for men "Lusto for Men " and women- "Lusto for Women" . Since the collection called Lusto will be used for both- we'd like the labels to look similar but separating the gender look- maybe by a same color variation. Our bottles are amber in color , so we like the beiges, cream, and earthy warm tones - greens- brown-orange- yellow-colors. The labels are for 8 oz amber cosmo round bottles. The height is 7.32inches and the diameter is 1.85 inches.
Our starting line will be Lusto for Men ( Silk Body Wash, Silk Body Lotion and Body Mist) and the same for Lusto for Women.
Updates

Target Market(s)

Our target audience is between 30 to 60 years of age. Salons and private consumers.
I am including attached sample of what was started by me.

Industry/Entity Type

Business

Requirements
Must have
• We would like to incorporate the company name- VaduMakers along with the name of the product- which will be Lusto for Men or Lusto for Women on each label.

On label with company name or somewhere on label we would like a tree to symbolize the beginning, but we are open to suggestions.

```html
<!DOCTYPE html>
<html lang="en">
<head>
<meta charset="utf-8">
<title>Lusto for Men – Silk Body Wash Labels</title>
<link rel="stylesheet" href="https://fonts.googleapis.com/css2?family=Cabin:wght@500;700&family=Crimson+Text:ital,wght@0,400;0,600;1,400&family=Arimo:wght@400;700&display=swap">
<style>
  :root {
    --page: #ffffff;
    --gold-light: #f6e7b0;
    --gold-mid: #d4ad55;
    --gold-dark: #9a7128;
    --caramel-top: #c99768;
    --caramel-mid: #b1703f;
    --caramel-low: #8f5129;
    --cream: #f8f0dc;
    --cream-edge: #e8cd92;
    --ink-brown: #4a2a12;
    --ink-dark: #2b1a0c;
    --label-white: #fffaf0;
    --leaf-pale: rgba(255, 244, 222, 0.55);
  }
  * { box-sizing: border-box; margin: 0; padding: 0; }
  html, body {
    width: 922px; height: 1200px; overflow: hidden;
    background: var(--page);
  }
  .canvas { position: relative; width: 922px; height: 1200px; }

  .label {
    position: absolute; top: 180px;
    width: 300px; height: 840px; border-radius: 50%;
    background: linear-gradient(135deg, var(--gold-light), var(--gold-mid) 35%, var(--gold-dark) 60%, var(--gold-light) 85%, var(--gold-mid));
    padding: 8px;
  }
  .label--front { left: 80px; }
  .label--back { left: 542px; }
  .label__face {
    position: relative; width: 100%; height: 100%;
    border-radius: 50%; overflow: hidden;
  }

  /* Front */
  .label--front .label__face {
    background: linear-gradient(180deg, var(--caramel-top) 0%, var(--caramel-mid) 50%, var(--caramel-low) 100%);
  }
  .tree-art {
    position: absolute; left: -10px; top: 70px; width: 230px; height: 340px;
    background: radial-gradient(ellipse at 45% 45%, var(--leaf-pale), rgba(255, 240, 215, 0.15) 60%, transparent 75%);
  }
  .branch-art {
    position: absolute; left: 70px; top: 640px; width: 220px; height: 140px;
    background: radial-gradient(ellipse at 60% 50%, rgba(240, 200, 150, 0.45), transparent 70%);
  }
  .brand-arc { position: absolute; left: 0; top: 0; width: 284px; height: 824px; }
  .brand-arc text {
    font-family: "Crimson Text", serif; font-size: 30px; fill: var(--ink-brown);
  }
  .product-name {
    position: absolute; top: 432px; width: 100%; text-align: center;
    font-family: "Cabin", sans-serif; font-weight: 700; font-size: 56px;
    letter-spacing: 3px; color: var(--label-white);
  }
  .product-gender {
    position: absolute; top: 500px; width: 100%; padding-left: 70px; text-align: center;
    font-family: "Crimson Text", serif; font-size: 30px; color: var(--ink-dark);
  }
  .product-type {
    position: absolute; top: 600px; width: 100%; text-align: center;
    font-family: "Cabin", sans-serif; font-weight: 500; font-size: 22px;
    letter-spacing: 1px; color: var(--cream);
  }
  .product-size {
    position: absolute; top: 770px; width: 100%; text-align: center;
    font-family: "Arimo", sans-serif; font-size: 12px; color: var(--ink-dark);
  }

  /* Back */
  .label--back .label__face {
    background: radial-gradient(ellipse at 50% 50%, var(--cream) 0%, var(--cream) 55%, var(--cream-edge) 100%);
  }
  .back-copy {
    position: absolute; top: 95px; left: 46px; right: 46px;
    text-align: center; color: var(--ink-dark);
  }
  .back-copy__intro {
    font-family: "Crimson Text", serif; font-style: italic; font-size: 18px; line-height: 1.25;
  }
  .back-copy__text {
    font-family: "Arimo", sans-serif; font-size: 13px; line-height: 1.3; margin-top: 18px;
  }
  .back-copy__ingredients {
    font-family: "Arimo", sans-serif; font-size: 8.5px; line-height: 1.3;
    text-align: left; margin-top: 20px; padding: 0 6px; font-style: italic;
  }
  .back-copy__ingredients strong { font-style: normal; }
  .back-copy__company {
    font-family: "Crimson Text", serif; font-style: italic; font-size: 17px;
    line-height: 1.2; margin-top: 18px;
  }
  .back-copy__city { font-family: "Arimo", sans-serif; font-size: 12px; }
  .back-copy__shop {
    font-family: "Arimo", sans-serif; font-size: 12px; line-height: 1.35; margin-top: 16px;
  }
</style>
</head>
<body>
<main class="canvas">

  <section class="label label--front" aria-label="Front label">
    <div class="label__face">
      <div class="tree-art" role="img" aria-label="Pale illustrated tree with leafy branches"></div>
      <div class="branch-art" role="img" aria-label="Illustrated leafy branch"></div>
      <svg class="brand-arc" viewBox="0 0 284 824" aria-label="VaduMakers">
        <path id="brand-curve" d="M122 38 A115 380 0 0 1 250 250" fill="none"/>
        <text><textPath href="#brand-curve">VaduMakers</textPath></text>
      </svg>
      <h1 class="product-name">LUSTO</h1>
      <p class="product-gender">for men</p>
      <p class="product-type">SILK BODY WASH</p>
      <p class="product-size">8.25 fl oz / 244mL</p>
    </div>
  </section>

  <section class="label label--back" aria-label="Back label">
    <div class="label__face">
      <div class="back-copy">
        <p class="back-copy__intro">Our Nourishing Silk Body Wash will engulf you in luxurious lather as it gently cleanses your delicate skin leaving it soft as silk.</p>
        <p class="back-copy__text">Directions: Apply to skin while damp with sponge or wash cloth. Rinse well.</p>
        <p class="back-copy__text">WARNINGS/CAUTIONS:<br>For external use only. Avoid contact with eyes.</p>
        <p class="back-copy__text">NOT TESTED ON ANIMALS</p>
        <p class="back-copy__ingredients"><strong>INGREDIENTS:</strong> purified water, sodium olefin sulfonate (plant source), organic aloe leaf juice, cocamidopropyl betaine (plant source), sodium chloride (salt), vegetable glycerin, tocopherol (vitamin E), polysorbate 20, potassium sorbate, phenoxyethanol (mild preservative), caprylyl glycol, organic chamomile extract, calendula flower extract, xanthan gum, magnesium ascorbyl phosphate (vitamin C ester), sodium bicarbonate (baking soda), citric acid, fragrance.</p>
        <p class="back-copy__company">VaduMakers<br>Bath – Body – Home</p>
        <p class="back-copy__city">Cedar Bay, FL 30418</p>
        <p class="back-copy__shop">Shop 24/7 -<br>www.vadumakers.com</p>
      </div>
    </div>
  </section>

</main>
</body>
</html>
```